Brindle - Web Design Rebrand for Manufacturing Automation Company

I need a new brand for a customer based in Ireland.
The website currently: https://corvanmotion.example/
Corvan Automation provides a wide range of automation and IT solutions used in manufacturing operations.
Their solutions span a broad spectrum of technology from physical machines and robots to cloud based management solutions for these systems.
They are an Authorised Distributor for Tessmark Automation.
Their partnership with Tessmark Automation will now include working closely to keep track of supply trends and preparing customers for future Data Centre projects.

Essentially their USP:
They have a large team of specialist technical people spanning the breadth of skills to be able to deploy and support automation and IT solutions in manufacturing in the Life Sciences Industry.

Along with Tessmark Automation, they have specialist teams for accelerating Data Center applications.

Competitor websites:
https://www.valdrenco.example/global/en.html - I really like the layout of their partnerships/collaborations section.
https://global.qmt.example/group/en - Their first moving imagery/tagline and 'discover more' when you enter the site is really eye-catching.
https://www.pk-energy.example/uk/en/ - They layout and structure of the 'The core of what we do section' is really nice.

These are a big companies so anything we could steal would be good 😊

They want:
• Fresh, sharp imagery
• Movement on the main page and perhaps video on some sections? - similar to QMT
• A page to showcase Automation Solutions
• A page to showcase Data Centers
• About us
• Sectors they operate in (includes Life Sciences, Food & Bev, Data Centres)

Life Science Manufacturing

1 page

Sans Serif

Colors
0054AA
0677BA
7BADD7
CADEEF
E8F1F8

Must have
• Moving Imagery

```html
<!DOCTYPE html>
<html lang="en">
<head>
<meta charset="utf-8">
<title>Corvan Automation</title>
<link rel="stylesheet" href="https://fonts.googleapis.com/css2?family=Exo+2:wght@500;600&family=Noto+Sans:wght@400;500&family=Rajdhani:wght@700&family=Roboto:wght@400;500&family=Montserrat:wght@500&display=swap">
<style>
:root{
  --navy:#1a1940;
  --footer:#0c1b3e;
  --cyan:#29a8df;
  --blue-deep:#0054aa;
  --blue-mid:#0677ba;
  --blue-soft:#7badd7;
  --ink:#333;
  --panel:#f2f5f7;
  --white:#fff;
}
*{margin:0;padding:0;box-sizing:border-box}
html,body{width:1200px;height:2560px;overflow:hidden}
body{position:relative;background:var(--white);font-family:'Noto Sans',sans-serif;color:var(--ink)}
.abs{position:absolute}

/* hero */
.hero{left:0;top:0;width:1200px;height:705px;background:var(--navy);clip-path:polygon(0 0,100% 0,100% 683px,0 703px)}
.hero-art{left:0;top:0;width:1200px;height:705px;background:radial-gradient(ellipse 90% 55% at 50% 95%,#1d6fb8 0%,#153f86 40%,transparent 75%),linear-gradient(180deg,#1a1940 0%,#1c2a66 55%,#1a4c94 100%)}
.brand{left:52px;top:32px;display:flex;align-items:center;gap:12px}
.brand-mark{width:20px;height:20px;background:var(--cyan)}
.brand-name{font-family:'Montserrat',sans-serif;font-weight:500;font-size:18px;letter-spacing:.5px;color:var(--cyan)}
.nav{right:54px;top:36px;display:flex;align-items:center;gap:39px;font-family:'Noto Sans',sans-serif;font-size:15px;color:var(--white)}
.nav-social{width:46px;height:42px;background:var(--cyan);border-radius:3px}
.hero-title{left:0;top:222px;width:1200px;text-align:center;color:var(--white);font-family:'Exo 2',sans-serif;font-weight:600}
.hero-title .l1{font-size:44px;line-height:54px}
.hero-title .l2{font-size:34px;line-height:42px;font-weight:500}
.hero-sub{left:0;top:330px;width:1200px;text-align:center;color:#d7def0;font-family:'Montserrat',sans-serif;font-size:19px;line-height:30px}
.btn-hero{left:520px;top:407px;width:161px;height:55px;background:var(--cyan);color:var(--white);border-radius:4px;font-family:'Montserrat',sans-serif;font-weight:500;font-size:15px;display:flex;align-items:center;justify-content:center}
.badge{top:510px;width:177px;height:91px;background:#111425;border-radius:6px}
.dots{left:578px;top:642px;display:flex;gap:6px}
.dots span{width:11px;height:11px;background:#8a93a8}
.dots span:first-child{background:var(--cyan)}

/* about */
.about-art{left:98px;top:870px;width:492px;height:340px;border-radius:20px;background:radial-gradient(ellipse 60% 45% at 50% 45%,#3a78b0 0%,#1f4d80 55%,#f3f5f8 100%)}
.about-title{left:624px;top:826px;font-family:'Exo 2',sans-serif;font-weight:500;font-size:44px;color:var(--cyan)}
.about-rule{left:1038px;top:847px}
.about-copy{left:624px;top:888px;width:485px;font-size:16px;line-height:26.5px;color:#3a3a3a}
.about-copy p{margin-bottom:12px}
.btn-outline{left:624px;top:1195px;width:165px;height:49px;border:2px solid var(--cyan);border-radius:25px;color:var(--cyan);font-family:'Montserrat',sans-serif;font-weight:500;font-size:16px;display:flex;align-items:center;justify-content:center}

/* solutions */
.solutions{left:0;top:1322px;width:1200px;height:625px;background:var(--panel)}
.sol-title{left:0;top:1383px;width:1200px;text-align:center;font-family:'Rajdhani',sans-serif;font-weight:700;font-size:29px;color:#111}
.sol-text{left:270px;top:1425px;width:660px;text-align:center;font-size:16px;line-height:27px;color:#444}
.sol-rule{left:556px;top:1497px;width:95px;height:4px;background:var(--cyan)}
.card{top:1553px;width:221px;height:287px;overflow:hidden}
.card-label{left:0;bottom:32px;width:100%;text-align:center;font-family:'Roboto',sans-serif;font-size:23px;color:var(--white)}
.card-label::before{content:"";display:block;width:22px;height:3px;background:var(--white);margin:0 auto 8px 48px}
.c1{left:148px;background:linear-gradient(180deg,#0b1e44,#174a8e 60%,#0b2454)}
.c2{left:379px;background:linear-gradient(180deg,#6b7f9a,#8a3c14 55%,#3a1a0c)}
.c3{left:609px;background:radial-gradient(ellipse at 60% 30%,#3d7fd6,#123a86 70%)}
.c4{left:838px;background:radial-gradient(ellipse at 50% 75%,#2f6fd0,#0f2358 70%)}

/* partners */
.partner{top:1982px;height:121px;display:flex;align-items:center;justify-content:center;font-family:'Noto Sans',sans-serif;font-weight:500;font-size:30px}
.p1{left:104px;width:223px;border:2px solid var(--cyan);color:#222}
.p2{left:360px;width:180px;color:#555}
.p3{left:610px;width:160px;color:var(--blue-deep)}
.p4{left:846px;width:180px;gap:10px;color:#222;font-size:18px}
.p4 i{width:40px;height:40px;border-radius:50%;background:#e0263b;display:block}

/* footer */
.footer{left:0;top:2155px;width:1200px;height:405px;background:var(--footer);color:var(--white)}
.f-brand{left:104px;top:2320px;font-family:'Montserrat',sans-serif;font-weight:500;font-size:20px;line-height:22px;color:var(--cyan)}
.f-brand span{color:#d6dbe6;display:block}
.f-sep{top:2237px;width:1px;height:170px;background:#2a3a5e}
.f-head{top:2242px;font-family:'Roboto',sans-serif;font-weight:500;font-size:17px}
.f-list{top:2285px;list-style:none;font-family:'Roboto',sans-serif;font-size:14px;line-height:25.5px;color:#c9cfdb}
.f-list li{display:flex;align-items:center;gap:11px}
.f-list li::before{content:"";width:12px;height:12px;border-radius:50%;background:#8c95a8}
.f-contact{font-family:'Roboto',sans-serif;font-size:16px;line-height:21px;color:#c9cfdb}
.f-contact b{font-weight:400;color:var(--white)}
.f-rule{left:100px;top:2447px;width:1005px;height:1px;background:#2a3a5e}
.f-copy{left:100px;top:2480px;font-family:'Roboto',sans-serif;font-size:14px;color:#a9b1c2}
.f-legal{right:95px;top:2480px;font-family:'Roboto',sans-serif;font-size:14px;color:var(--white)}
</style>
</head>
<body>

<header class="abs hero">
  <div class="abs hero-art" role="img" aria-label="Glowing blue digital data landscape with rising light particles"></div>
</header>
<div class="abs brand"><i class="brand-mark"></i><span class="brand-name">CORVAN AUTOMATION</span></div>
<nav class="abs nav">
  <span>HROBOTICS &amp; AUTOMATION SOLUTIONS</span><span>ABOUT</span><span>CONTACT</span><i class="nav-social"></i>
</nav>
<h1 class="abs hero-title"><div class="l1">Your Automation,</div><div class="l2">IT and Data Centre Solutions Provider</div></h1>
<p class="abs hero-sub">A Tessmark Automation Distributor Specialising<br>in Life Sciences and Data Centres.</p>
<a class="abs btn-hero">CONTACT US</a>
<div class="abs badge" style="left:420px"></div>
<div class="abs badge" style="left:604px"></div>
<div class="abs dots"><span></span><span></span><span></span></div>

<section>
  <div class="abs about-art" role="img" aria-label="Floating isometric tiles showing circuit and technology imagery"></div>
  <h2 class="abs about-title">Corvan Automation</h2>
  <svg class="abs about-rule" width="162" height="16" viewBox="0 0 162 16"><circle cx="6" cy="8" r="5" fill="#0677ba"/><line x1="12" y1="8" x2="162" y2="8" stroke="#0677ba" stroke-width="1.5" stroke-dasharray="4 3"/></svg>
  <div class="abs about-copy">
    <p>provides a wide range of automation and IT solutions used in manufacturing operations.</p>
    <p>Our solutions span a broad spectrum of technology from physical machines and robots to cloud based management solutions for these systems. Along with Tessmark Automation, we work closely to keep track of supply trends and invest wisely to prepare for customers' future DC projects.</p>
    <p>We have a large team of specialist technical people spanning the breadth of skills to be able to deploy and support these technologies.</p>
  </div>
  <a class="abs btn-outline">READ MORE</a>
</section>

<section class="abs solutions"></section>
<h2 class="abs sol-title">ROBOTICS AND AUTOMATION SOLUTIONS</h2>
<p class="abs sol-text">Lorem Ipsum is simply dummy text of the printing and typesetting industry. Lorem Ipsum has been the industry's standard dummy text ever since the 1500s,</p>
<div class="abs sol-rule"></div>
<div class="abs card c1" role="img" aria-label="Server racks in a blue-lit data centre aisle"><div class="abs card-label">Data Centres</div></div>
<div class="abs card c2" role="img" aria-label="Bottles on a beverage production line"><div class="abs card-label">Food &amp; Beverage</div></div>
<div class="abs card c3" role="img" aria-label="Blue molecular network structure"><div class="abs card-label">Life Sciences</div></div>
<div class="abs card c4" role="img" aria-label="Digital city skyline with connected icons"><div class="abs card-label">IT Infrastructure</div></div>

<div class="abs partner p1">Kelvara</div>
<div class="abs partner p2">ostrilink</div>
<div class="abs partner p3">MARAVEL</div>
<div class="abs partner p4"><i></i>Tessmark</div>

<footer class="abs footer"></footer>
<div class="abs f-brand">CORVAN<span>AUTOMATION</span></div>
<div class="abs f-sep" style="left:313px"></div>
<div class="abs f-sep" style="left:539px"></div>
<div class="abs f-sep" style="left:803px"></div>
<h3 class="abs f-head" style="left:364px">QUICK LINKS</h3>
<ul class="abs f-list" style="left:364px"><li>Home</li><li>LInk</li><li>About Us</li><li>Sitemap</li><li>Automation</li></ul>
<h3 class="abs f-head" style="left:607px">ACCOUNT</h3>
<ul class="abs f-list" style="left:607px"><li>Login</li><li>Account</li><li>Support</li><li>Privacy Policy</li><li>Terms &amp; Conditions</li></ul>
<h3 class="abs f-head" style="left:859px">CONTACT</h3>
<svg class="abs" style="left:871px;top:2282px" width="28" height="22" viewBox="0 0 28 22"><rect x="1" y="1" width="26" height="20" fill="none" stroke="#8c95a8" stroke-width="1.5"/><polyline points="1,1 14,12 27,1" fill="none" stroke="#8c95a8" stroke-width="1.5"/></svg>
<div class="abs f-contact" style="left:917px;top:2272px"><b>Email:</b><br>name@corvanmail.example</div>
<svg class="abs" style="left:873px;top:2373px" width="24" height="30" viewBox="0 0 24 30"><path d="M12 29C12 29 2 17 2 11a10 10 0 0 1 20 0c0 6-10 18-10 18z" fill="none" stroke="#8c95a8" stroke-width="1.5"/><circle cx="12" cy="11" r="4" fill="none" stroke="#8c95a8" stroke-width="1.5"/></svg>
<div class="abs f-contact" style="left:920px;top:2346px"><b>Address</b><br>48 Harbour Quay Unit 12<br>Dunmore, DM 40217</div>
<div class="abs f-rule"></div>
<div class="abs f-copy">Copyright @ Corvan 2024</div>
<div class="abs f-legal">Cookie policy &nbsp;<span style="color:#8c95a8">|</span>&nbsp;&nbsp; Terms of Condition</div>

</body>
</html>
```